Casa Vero Inspections Business Card

I need a business card for my new company. The company is going to provide home inspections. The name of the company is Casa Vero Inspections. I am not sure if I want a single sided card or a double. I have a logo already that I want to incorporate into the card design. I was wondering if I should incorporate a catch phrase on my card or not. If I did the phrase would be "Careful Eyes on Every Corner of Your Home" but i am unsure how or if to use it on a card. The following information needs to be on the card.
Home Inspection
My Name: Marcus T. Wolford Phone Number: 555-301-7762 Email: mwolford@casaveroinspections.com Website: www.casaveroinspections.com NY HI License # 27300519462

```html
<!DOCTYPE html>
<html lang="en">
<head>
<meta charset="utf-8">
<title>Casa Vero Inspections – Business Card</title>
<link rel="stylesheet" href="https://fonts.googleapis.com/css2?family=Montserrat:wght@400;600;700&display=swap">
<style>
  :root {
    --bg: #9a9a9a;
    --brand-blue: #0569a8;
    --brand-blue-back: #0c6dad;
    --brand-blue-deep: #0a5f99;
    --white: #ffffff;
  }
  * { margin: 0; padding: 0; box-sizing: border-box; }
  html, body {
    width: 1093px; height: 1200px; overflow: hidden;
    background: var(--bg);
    font-family: "Montserrat", sans-serif;
  }
  .card {
    position: absolute;
    border-radius: 18px;
    overflow: hidden;
  }
  .card--front { top: 225px; left: 264px; width: 581px; height: 363px; background: var(--white); }
  .card--back  { top: 616px; left: 259px; width: 595px; height: 366px; background: var(--brand-blue-back); }

  .wordmark {
    position: absolute; left: 0; right: 0;
    text-align: center;
    font-weight: 700;
    color: var(--brand-blue);
    line-height: 1;
  }
  .wordmark__main { display: block; font-size: 50px; letter-spacing: 1px; }
  .wordmark__sub  { display: block; font-size: 20px; letter-spacing: 6px; margin-top: 12px; }
  .card--front .wordmark { top: 70px; }

  .contact-band {
    position: absolute; left: 0; right: 0; bottom: 0;
    height: 125px;
    background: var(--brand-blue);
    color: var(--white);
  }
  .holder-name {
    position: absolute; right: 323px; top: 36px;
    font-size: 20px; font-weight: 700; white-space: nowrap;
  }
  .band-divider {
    position: absolute; left: 270px; top: 16px;
    width: 1px; height: 64px; background: var(--white);
  }
  .contact-list { position: absolute; left: 282px; top: 12px; list-style: none; }
  .contact-list li {
    display: flex; align-items: center;
    height: 24.5px; font-size: 13px; font-weight: 400;
  }
  .contact-list svg { width: 13px; height: 13px; margin-right: 14px; fill: var(--white); }
  .license {
    position: absolute; left: 0; right: 0; top: 97px;
    text-align: center; font-size: 12.5px; padding-right: 50px;
  }

  .card--back .wordmark { top: 130px; color: var(--brand-blue-deep); }
  .card--back .wordmark__main { font-size: 58px; }
  .card--back .wordmark__sub { font-size: 22px; }
  .tagline {
    position: absolute; left: 0; right: 0; top: 316px;
    text-align: center; color: var(--white);
    font-size: 13.5px; font-weight: 700; padding-right: 24px;
  }
</style>
</head>
<body>
  <section class="card card--front">
    <h1 class="wordmark">
      <span class="wordmark__main">CASA VERO</span>
      <span class="wordmark__sub">INSPECTIONS</span>
    </h1>
    <div class="contact-band">
      <p class="holder-name">Marcus T. Wolford</p>
      <span class="band-divider"></span>
      <ul class="contact-list">
        <li>
          <svg viewBox="0 0 24 24" aria-hidden="true"><path d="M6.6 10.8a15.1 15.1 0 0 0 6.6 6.6l2.2-2.2c.3-.3.7-.4 1-.2 1.1.4 2.3.6 3.6.6.6 0 1 .4 1 1V20c0 .6-.4 1-1 1A17 17 0 0 1 3 4c0-.6.4-1 1-1h3.5c.6 0 1 .4 1 1 0 1.3.2 2.5.6 3.6.1.3 0 .7-.2 1z"/></svg>
          555-301-7762
        </li>
        <li>
          <svg viewBox="0 0 24 24" aria-hidden="true"><path d="M2 5h20v2l-10 6L2 7zM2 9l10 6 10-6v10H2z"/></svg>
          mwolford@casaveroinspections.com
        </li>
        <li>
          <svg viewBox="0 0 24 24" aria-hidden="true"><path d="M12 2a10 10 0 1 0 0 20 10 10 0 0 0 0-20zm-1 17.9A8 8 0 0 1 4.2 10L9 14.8v1a2 2 0 0 0 2 2zm6.9-2.5A2 2 0 0 0 16 16h-1v-3a1 1 0 0 0-1-1H8v-2h2a1 1 0 0 0 1-1V7h2a2 2 0 0 0 2-2v-.4a8 8 0 0 1 2.9 12.8z"/></svg>
          www.casaveroinspections.com
        </li>
      </ul>
      <p class="license">NY HI License # 27300519462</p>
    </div>
  </section>

  <section class="card card--back">
    <p class="wordmark">
      <span class="wordmark__main">CASA VERO</span>
      <span class="wordmark__sub">INSPECTIONS</span>
    </p>
    <p class="tagline">Careful Eyes on Every Corner of Your Home</p>
  </section>
</body>
</html>
```